Im open to ideas.. I was thinking on my business cards aswell as my logo. a place for my name. email. phone number and abn..

ive attched a file with my business logo. which i dont love the colours.. i was think a dark background with charcoal letters so something along those colour schumes but im open to ideas..

Business

BRL Constructions

```html
<!DOCTYPE html>
<html lang="en">
<head>
<meta charset="utf-8">
<title>BRL Constructions – Business Card</title>
<link href="https://fonts.googleapis.com/css2?family=Lato:wght@400;700;900&display=swap" rel="stylesheet">
<style>
  :root {
    --backdrop: #2b2b2b;
    --card: #f7f7f7;
    --ink: #1c1c1c;
    --ink-soft: #333333;
    --brand-red: #c4161c;
    --brand-red-dark: #9e1016;
    --map-grey: #d9d9d9;
    --map-pink: #f1d3d3;
  }
  * { box-sizing: border-box; margin: 0; padding: 0; }
  html, body {
    width: 1200px; height: 873px; overflow: hidden;
    background: var(--backdrop);
    font-family: "Lato", sans-serif;
  }
  .card {
    position: absolute; left: 180px; top: 196px;
    width: 840px; height: 480px;
    background: var(--card);
    overflow: hidden;
    box-shadow: 0 20px 50px rgba(0,0,0,.5);
  }
  .world-map {
    position: absolute; left: 130px; top: 70px;
    width: 600px; height: 290px;
    border-radius: 40px;
    background: radial-gradient(ellipse at 50% 50%, var(--map-pink) 0%, var(--map-grey) 55%, rgba(217,217,217,0) 80%);
    opacity: .55;
  }
  .brand {
    position: absolute; left: 0; right: 0; top: 58px;
    text-align: center;
    font-weight: 900; font-size: 46px; letter-spacing: 1px;
    color: var(--ink);
  }
  .brand-mark {
    display: inline-block; width: 22px; height: 22px;
    background: var(--brand-red); margin-right: 14px; vertical-align: 4px;
  }
  .person { position: absolute; left: 110px; top: 250px; text-align: right; width: 250px; }
  .person-name { font-weight: 700; font-size: 27px; color: var(--brand-red); }
  .person-role { font-size: 20px; color: var(--ink-soft); margin-top: 6px; }
  .divider {
    position: absolute; left: 395px; top: 185px; width: 3px; height: 150px;
    background: linear-gradient(to bottom, rgba(196,22,28,0), var(--brand-red) 50%, rgba(196,22,28,0));
  }
  .contacts { position: absolute; left: 425px; top: 180px; list-style: none; }
  .contacts li {
    display: flex; align-items: center; gap: 14px;
    font-size: 20px; color: var(--ink); height: 38px;
  }
  .contacts svg { width: 20px; height: 20px; fill: none; stroke: var(--brand-red); stroke-width: 2; }
  .contacts .solid { fill: var(--brand-red); stroke: none; }
  .address {
    position: absolute; left: 0; right: 0; top: 385px;
    text-align: center; font-weight: 700; font-size: 24px; color: var(--brand-red);
  }
  .bottom-bands { position: absolute; left: 0; bottom: 0; width: 840px; height: 60px; }
</style>
</head>
<body>
  <div class="card">
    <div class="world-map" role="img" aria-label="Dotted world map in soft grey and pink"></div>

    <div class="brand"><span class="brand-mark"></span>BRL Constructions</div>

    <div class="person">
      <div class="person-name">Daniel R Moss</div>
      <div class="person-role">Managing Partner</div>
    </div>

    <div class="divider"></div>

    <ul class="contacts">
      <li>
        <svg viewBox="0 0 24 24"><path class="solid" d="M3 9c0-3 4-5 9-5s9 2 9 5v2h-5V9H8v2H3zM6 12h12l2 8H4z"/></svg>
        +1 (555) 214-3087
      </li>
      <li>
        <svg viewBox="0 0 24 24"><rect x="6" y="2" width="12" height="20" rx="2"/><line x1="10" y1="18" x2="14" y2="18"/></svg>
        +1 (555) 607-4912
      </li>
      <li>
        <svg viewBox="0 0 24 24"><rect class="solid" x="2" y="5" width="20" height="14"/><path d="M2 5l10 8 10-8" stroke="#fff"/></svg>
        dmoss@brlbuild.com
      </li>
      <li>
        <svg viewBox="0 0 24 24"><path d="M10 14a4 4 0 0 0 6 0l4-4a4 4 0 0 0-6-6l-1 1M14 10a4 4 0 0 0-6 0l-4 4a4 4 0 0 0 6 6l1-1"/></svg>
        www.brlbuild.com
      </li>
    </ul>

    <div class="address">48 Cedar Ridge Road, 2nd Floor, Fairview, CT 06118</div>

    <svg class="bottom-bands" viewBox="0 0 840 60" preserveAspectRatio="none">
      <path d="M0 42 L560 42 Q580 42 590 34 L600 28 L840 28 L840 60 L0 60 Z" fill="var(--ink)"/>
      <path d="M600 28 Q612 14 640 14 L840 14 L840 60 L585 60 Q590 40 600 28 Z" fill="var(--brand-red)"/>
    </svg>
  </div>
</body>
</html>
```